B2B modern industry lubrication label

We are a chemical company that needs a new, very modern outstanding lubrication packaging label. The logo attached can be changed in color. The name of the product is R83. Attached also the text you can use, please disregard the current layout of the text, you can make it any layout you want. Be free in font type, colors and other design aspects.
Dimensions: 21 x 14,8 cm
Target Market(s)
industry, companies with machinery
Industry/Entity Type
Industrial
Colors
Designer to choose colors to be used in the design.
Look and feel
Each slider illustrates characteristics of the customer's brand and the style your logo design should communicate.

```html
<!DOCTYPE html>
<html lang="en">
<head>
<meta charset="utf-8">
<title>R83 Pro spray label</title>
<link rel="stylesheet" href="https://fonts.googleapis.com/css2?family=Arimo:wght@400;700&family=Oswald:wght@600;700&display=swap">
<style>
  :root {
    --backdrop: #2b2b2b;
    --paper: #ffffff;
    --ink: #111111;
    --orange: #f7941d;
    --orange-deep: #f26a21;
    --red: #ee4423;
    --yellow: #fdc113;
    --peach: #fbb27a;
  }
  * { box-sizing: border-box; margin: 0; padding: 0; }
  html, body { width: 1200px; height: 999px; overflow: hidden; }
  body { background: var(--backdrop); font-family: "Arimo", Arial, sans-serif; color: var(--ink); }

  .label {
    position: absolute; left: 213px; top: 70px;
    width: 782px; height: 857px;
    background: var(--paper); overflow: hidden;
  }
  .label-art { position: absolute; inset: 0; width: 782px; height: 857px; }

  .brand {
    position: absolute; font-family: "Oswald", "Arial Narrow", sans-serif;
    font-weight: 700; color: var(--orange-deep); letter-spacing: 1px; line-height: 1;
    text-align: center;
  }
  .brand--small { left: 95px; top: 28px; width: 205px; font-size: 42px; }
  .brand--large { left: 470px; top: 100px; width: 230px; font-size: 58px; }

  .product-name {
    position: absolute; left: 400px; top: 252px; width: 370px; text-align: center;
    font-family: "Oswald", "Arial Narrow", sans-serif; font-weight: 700;
    font-size: 80px; line-height: 1; color: var(--orange); letter-spacing: 3px;
  }
  .product-form {
    position: absolute; left: 400px; top: 348px; width: 370px; text-align: center;
    font-weight: 700; font-size: 32px; line-height: 1;
  }

  .section { position: absolute; left: 23px; width: 347px; font-size: 14px; line-height: 18px; }
  .section h2 { font-size: 18px; font-weight: 700; margin-bottom: 12px; line-height: 1; }
  .section p { text-align: justify; }
  .section--application { top: 103px; }
  .section--instructions { top: 402px; }
  .section--advantages { top: 582px; }
  .section ul { list-style: none; width: 340px; }
  .section--advantages ul { width: 320px; }
  .section li { position: relative; padding-left: 27px; }
  .section li::before {
    content: ""; position: absolute; left: 2px; top: 5px;
    width: 7px; height: 7px; border-radius: 50%; background: var(--ink);
  }
  .section--advantages li { margin-bottom: 1px; }

  .specs { position: absolute; left: 412px; top: 562px; font-size: 14px; }
  .specs h2 { font-size: 18px; font-weight: 700; margin-bottom: 10px; line-height: 1; }
  .specs table { border-collapse: collapse; }
  .specs td { padding: 0 0 7px 0; height: 25px; vertical-align: top; }
  .specs td:first-child { width: 135px; }
</style>
</head>
<body>
  <main class="label">
    <svg class="label-art" viewBox="0 0 782 857" aria-hidden="true">
      <defs>
        <linearGradient id="tint" x1="0" y1="0" x2="1" y2="1">
          <stop offset="0" stop-color="#f9a25a"/>
          <stop offset="0.5" stop-color="#fcc88e"/>
          <stop offset="1" stop-color="#fde6c2"/>
        </linearGradient>
        <linearGradient id="flare" x1="0" y1="0" x2="0" y2="1">
          <stop offset="0" stop-color="var(--orange-deep)"/>
          <stop offset="0.55" stop-color="var(--orange)"/>
          <stop offset="1" stop-color="var(--yellow)"/>
        </linearGradient>
      </defs>
      <!-- left tinted panel -->
      <path d="M0,0 L390,0 L390,180 C250,260 80,400 0,555 Z" fill="url(#tint)"/>
      <!-- sweeping stripes from lower left to top right -->
      <path d="M-10,575 C90,300 320,70 800,14" fill="none" stroke="var(--peach)" stroke-width="16"/>
      <path d="M-10,562 C90,290 320,60 800,6" fill="none" stroke="var(--orange)" stroke-width="9"/>
      <path d="M-10,552 C90,282 320,52 800,-1" fill="none" stroke="var(--red)" stroke-width="4"/>
      <path d="M390,0 C520,-6 660,2 800,22 L800,-10 L390,-10 Z" fill="var(--yellow)"/>
      <!-- soft veil keeping the left panel light behind the copy -->
      <rect x="0" y="0" width="390" height="857" fill="#ffffff" opacity="0.5"/>
      <!-- right sweeping flare -->
      <path d="M800,200 C790,540 660,780 420,870 L800,870 Z" fill="url(#flare)"/>
      <path d="M800,200 C790,540 660,780 420,870" fill="none" stroke="var(--orange-deep)" stroke-width="8"/>
      <path d="M800,260 C790,580 670,790 470,870" fill="none" stroke="var(--red)" stroke-width="4"/>
      <path d="M800,320 C792,610 690,795 530,870" fill="none" stroke="#fbb040" stroke-width="12" opacity="0.8"/>
    </svg>

    <div class="brand brand--small">KORVANT</div>
    <div class="brand brand--large">KORVANT</div>

    <h1 class="product-name">R83 PRO</h1>
    <div class="product-form">(spray)</div>

    <section class="section section--application">
      <h2>Application:</h2>
      <p>R83 Pro is a high grade multifunctional product for lubrication and protection product.<br>
      R83 Pro is composed out of high grade synthetic oils, E.P. additives and penetrants. Also the product contains rust-preventing and waterproof substances. Practical experience proofed that R83 Pro cleans, lubricates and protects equipment, hinges, cables, conveyer belts, chains and other moving parts in machines and device excellently. R83 Pro cleans fats, resins and rust on the surface of materials.<br>
      R83 Pro create a good and durable lubrication. Even under circumstances with extreme pressure.<br>
      R83 Pro protects against moisture and rust.</p>
    </section>

    <section class="section section--instructions">
      <h2>Instructions for use:</h2>
      <ul>
        <li>Short shake before use</li>
        <li>Spray a thin layer of R83 Pro on the surface. The product will come out as a white, fast disappearing foam.</li>
        <li>Let R83 Pro do its work for a few minutes.</li>
        <li>Own evaluation for necessity and result.</li>
      </ul>
    </section>

    <section class="section section--advantages">
      <h2>Special advantages:</h2>
      <ul>
        <li>R83 Pro drives off the eventually present moisture.</li>
        <li>R83 Pro can handle temperatures until 370˚C.</li>
        <li>R83 Pro reaches even the smallest corners. This is because of the pressure of the spray, foaming and presence of high grade penetrants.</li>
        <li>R83 Pro forms an extremely thin and smooth layer of grease (Fw value: 0,1).</li>
        <li>R83 Pro helps prevent “pitting wear”.</li>
        <li>With use in propulsions, the starting couple will be lowered.</li>
      </ul>
    </section>

    <section class="specs">
      <h2>Specifications:</h2>
      <table>
        <tr><td>Colour:</td><td>Yellow</td></tr>
        <tr><td>Density:</td><td>1,07 g/ml</td></tr>
        <tr><td>Temperature range:</td><td>-40 until 370˚C</td></tr>
      </table>
    </section>
  </main>
</body>
</html>
```